Steadfast MD - Sleep Medicine Specialist - Business Cards

We are a new medical practice called Steadfast MD. We are sleep medicine specialists and we will be conducting sleep studies on patients with sleep related ailments. We want the business card to be bold, professional, and clean with the logo as the stand out visual piece. We dont like wild flashy designs. We want our design to be bold and classic while at the same time conveying who we are and what we do. We are reliable, professional, and the best in the business.

Industry/Entity Type

Health Care

Contact Information for Business Card

- Clean
- Bold
- Classic
- not cluttered

Requirements
Must have
• logo, website, phone number
Nice to have
• several options to choose from
Should not have
• flashy imaged - reflective print - images of people sleeping

```html
<!DOCTYPE html>
<html lang="en">
<head>
<meta charset="utf-8">
<title>Steadfast MD – Business Cards</title>
<link href="https://fonts.googleapis.com/css2?family=Archivo+Black&family=Roboto:wght@400;500&display=swap" rel="stylesheet">
<style>
  :root {
    --brand-red: #e0141c;
    --brand-red-faint: #f3cdd0;
    --ink: #0d0d0d;
    --card-black: #050505;
    --card-white: #f7f7f7;
    --text-grey: #2a2a2a;
    --backdrop: #e9e7e4;
  }
  * { box-sizing: border-box; margin: 0; padding: 0; }
  html, body { width: 1200px; height: 960px; overflow: hidden; }
  body {
    background: var(--backdrop);
    display: flex;
    flex-direction: column;
    align-items: center;
    justify-content: center;
    gap: 40px;
    font-family: "Roboto", Arial, sans-serif;
  }
  .card {
    position: relative;
    width: 760px;
    height: 434px;
    overflow: hidden;
    box-shadow: 0 6px 18px rgba(0,0,0,0.12);
  }
  .card--front { background: var(--card-black); }
  .card--back { background: var(--card-white); }

  .ring { position: absolute; border-radius: 50%; }
  .card--front .ring {
    width: 380px; height: 380px;
    left: -120px; top: 40px;
    border: 13px solid var(--brand-red);
  }
  .card--back .ring {
    width: 340px; height: 340px;
    right: -140px; top: -100px;
    border: 11px solid var(--brand-red-faint);
  }

  .wordmark {
    font-family: "Archivo Black", "Arial Black", sans-serif;
    letter-spacing: -1px;
    white-space: nowrap;
  }
  .card--front .wordmark {
    position: absolute;
    right: 44px; top: 150px;
    font-size: 56px;
    color: #ffffff;
  }

  .back-brand {
    position: absolute;
    left: 70px; top: 80px;
    display: flex; align-items: center; gap: 14px;
  }
  .back-brand__dot {
    width: 66px; height: 66px;
    border-radius: 50%;
    border: 6px solid var(--brand-red);
    flex: none;
  }
  .back-brand .wordmark { font-size: 42px; color: var(--ink); }

  .person {
    position: absolute;
    left: 92px; top: 186px;
  }
  .person__name {
    font-family: "Archivo Black", "Arial Black", sans-serif;
    font-size: 26px;
    color: var(--ink);
  }
  .person__name .surname { color: var(--brand-red); }
  .person__role {
    font-size: 24px; font-weight: 500;
    color: var(--text-grey);
    margin-top: 2px;
  }

  .accent-bar {
    position: absolute;
    left: 0; top: 258px;
    width: 50px; height: 44px;
    background: var(--brand-red);
  }

  .contact {
    position: absolute;
    left: 130px; top: 262px;
    list-style: none;
  }
  .contact li {
    display: flex; align-items: center; gap: 12px;
    font-size: 25px;
    color: var(--text-grey);
    line-height: 38px;
  }
  .contact svg { width: 22px; height: 22px; flex: none; }
</style>
</head>
<body>

  <section class="card card--front" aria-label="Business card front">
    <div class="ring"></div>
    <div class="wordmark">Steadfast MD</div>
  </section>

  <section class="card card--back" aria-label="Business card back">
    <div class="ring"></div>

    <div class="back-brand">
      <div class="back-brand__dot"></div>
      <div class="wordmark">Steadfast MD</div>
    </div>

    <div class="person">
      <div class="person__name">DANIEL <span class="surname">WHITCOMBE</span></div>
      <div class="person__role">Managing Director</div>
    </div>

    <div class="accent-bar"></div>

    <ul class="contact">
      <li>
        <svg viewBox="0 0 24 24" aria-hidden="true"><path fill="#e0141c" d="M6.6 10.8a15.1 15.1 0 0 0 6.6 6.6l2.2-2.2a1 1 0 0 1 1-.25 11.4 11.4 0 0 0 3.6.57 1 1 0 0 1 1 1V20a1 1 0 0 1-1 1A17 17 0 0 1 3 4a1 1 0 0 1 1-1h3.5a1 1 0 0 1 1 1c0 1.25.2 2.45.57 3.57a1 1 0 0 1-.25 1z"/></svg>
        020 7946 0182
      </li>
      <li>
        <svg viewBox="0 0 24 24" aria-hidden="true"><rect x="2" y="5" width="20" height="14" rx="2" fill="#e0141c"/><path d="M3 6l9 7 9-7" fill="none" stroke="#fff" stroke-width="2"/></svg>
        info@SteadfastMD.com
      </li>
      <li>
        <svg viewBox="0 0 24 24" aria-hidden="true"><circle cx="12" cy="12" r="10" fill="#e0141c"/><path d="M2 12h20M12 2c3 3 3 17 0 20M12 2c-3 3-3 17 0 20" fill="none" stroke="#fff" stroke-width="1.5"/></svg>
        www.SteadfastMD.com
      </li>
    </ul>
  </section>

</body>
</html>
```